Bay Bolts

I am starting a sharpening service for knives, scissors, and garden tools. It's a sole proprietorship, so it's a small business. The business name is "Bay Bolt." A one or two-page website is fine. Mark Orchard has created a logo for me. There should be pictures of the things I sharpen. There will also be a price list for sharpened items. My address is: 18302 Pellman Way, Stevenson Ranch, CA 91381. Phone number is 661-555-0173

```html
<!DOCTYPE html>
<html lang="en">
<head>
<meta charset="utf-8">
<title>Bay Bolt — Professional Sharpening</title>
<link href="https://fonts.googleapis.com/css2?family=Playfair+Display:wght@400;600;700&family=Lato:wght@300;400;700&display=swap" rel="stylesheet">
<style>
:root{
  --ink:#141414;
  --text:#3d3d3d;
  --muted:#666;
  --gold:#c9a25a;
  --gold-dark:#b08a45;
  --soft:#f7f9fb;
  --line:#e6e6e6;
  --white:#fff;
}
*{box-sizing:border-box;margin:0;padding:0}
html,body{width:1200px;height:3388px;overflow:hidden}
body{font-family:'Lato',sans-serif;color:var(--text);background:var(--white);position:relative}

.site-nav{position:absolute;top:0;left:0;width:1200px;height:74px;background:var(--ink);display:flex;align-items:center;justify-content:space-between;padding:0 60px;z-index:2}
.brand{font-family:'Playfair Display',serif;font-weight:600;font-size:23px;color:var(--white)}
.nav-links{display:flex;gap:28px;list-style:none}
.nav-links li{font-size:13px;letter-spacing:1px;color:#e8e8e8}

.hero{position:absolute;top:74px;left:0;width:1200px;height:564px;background:radial-gradient(ellipse at 75% 60%,#5a4630 0%,#2a241d 40%,#151310 80%)}
.hero-copy{position:absolute;left:60px;top:117px;width:700px}
.hero h1{font-family:'Playfair Display',serif;font-weight:700;font-size:56px;line-height:66px;color:var(--white)}
.hero p{margin-top:26px;font-size:18px;font-weight:300;color:#ddd}
.btn-call{display:inline-block;margin-top:36px;background:var(--gold);color:var(--ink);font-size:14px;padding:17px 28px;border-radius:3px}

.about{position:absolute;top:638px;left:0;width:1200px;height:689px}
.about-copy{position:absolute;left:60px;top:150px;width:520px}
.section-title{font-family:'Playfair Display',serif;font-weight:700;color:var(--ink)}
.about h2{font-size:34px;line-height:38px;width:540px}
.rule{width:75px;height:3px;background:var(--gold);margin-top:20px}
.about p{font-size:16px;line-height:27px;margin-top:26px;width:505px}
.about p+p{margin-top:22px}
.about-frame{position:absolute;left:645px;top:105px;width:510px;height:510px;border:2px solid var(--gold)}
.about-photo{position:absolute;left:630px;top:90px;width:510px;height:510px;background:linear-gradient(160deg,#5c5c5c,#2b2b2b 55%,#4a4a4a);box-shadow:0 6px 18px rgba(0,0,0,.2)}

.services{position:absolute;top:1327px;left:0;width:1200px;height:610px;background:var(--soft)}
.center-title{text-align:center;font-size:36px}
.services .center-title{margin-top:92px}
.rule-center{width:60px;height:3px;background:var(--gold);margin:18px auto 0}
.cards{position:absolute;left:60px;top:207px;display:flex;gap:38px}
.card{width:334px;height:314px;background:var(--white);border-top:4px solid var(--gold);box-shadow:0 4px 12px rgba(0,0,0,.08);text-align:center;padding:52px 36px 0}
.card svg{width:46px;height:46px}
.card h3{font-family:'Playfair Display',serif;font-weight:600;font-size:22px;color:var(--ink);margin-top:24px}
.card p{font-size:14px;line-height:24px;color:var(--muted);margin-top:16px}

.pricing{position:absolute;top:1937px;left:0;width:1200px;height:607px}
.pricing .center-title{margin-top:92px}
.price-list{position:absolute;left:247px;top:196px;width:706px;list-style:none}
.price-list li{display:flex;justify-content:space-between;align-items:center;height:55px;border-bottom:1px solid var(--line)}
.item{font-family:'Playfair Display',serif;font-size:17px;color:var(--ink)}
.cost{font-size:19px;font-weight:700;color:var(--gold-dark)}
.note{position:absolute;top:500px;left:0;width:1200px;text-align:center;font-size:12px;color:var(--muted)}

.contact{position:absolute;top:2544px;left:0;width:1200px;height:720px;background:linear-gradient(180deg,#8a8178 0%,#d9d6d1 30%,#c7c2bb 70%,#6d655c 100%)}
.contact-panel{position:absolute;left:60px;top:91px;width:1080px;height:521px;background:rgba(240,240,240,.95);border-radius:16px}
.form{position:absolute;left:39px;top:40px;width:478px}
.form h2{font-size:29px}
.field-label{display:block;font-size:12px;color:#444;margin-top:26px}
.form h2+.field-label{margin-top:24px}
.input{margin-top:8px;height:46px;border:1px solid #ddd;background:#fafafa;font-size:15px;color:#666;padding:13px 12px}
.input.area{height:114px}
.send{margin-top:23px;height:45px;background:var(--gold);color:var(--ink);font-size:14px;letter-spacing:.5px;display:flex;align-items:center;justify-content:center;border-radius:2px}
.visit{position:absolute;left:562px;top:40px;width:478px}
.visit h3{font-size:23px}
.visit .biz{margin-top:20px;font-size:15px}
.visit address{font-style:normal;font-size:14px;line-height:23px;margin-top:10px}
.visit .phone{margin-top:14px;font-size:17px;font-weight:700;color:var(--gold-dark)}
.map{position:absolute;left:562px;top:244px;width:478px;height:238px;border:1px solid #ddd;border-radius:4px;background:linear-gradient(135deg,#efe7d6,#dfe9cf 50%,#f3efe5)}

.site-footer{position:absolute;top:3264px;left:0;width:1200px;height:124px;background:var(--ink);padding:0 60px;display:flex;justify-content:space-between;align-items:center}
.footer-brand{font-family:'Playfair Display',serif;font-weight:600;font-size:23px;color:var(--white)}
.footer-tag{font-size:12px;color:var(--gold);margin-top:4px}
.footer-meta{text-align:right;font-size:12px;line-height:22px;color:#888}
</style>
</head>
<body>

<nav class="site-nav">
  <div class="brand">Bay Bolt</div>
  <ul class="nav-links"><li>HOME</li><li>ABOUT</li><li>SERVICES</li><li>PRICING</li><li>CONTACT</li></ul>
</nav>

<header class="hero" role="img" aria-label="Photo of a knife blade being sharpened on a grinding wheel with sparks">
  <div class="hero-copy">
    <h1>Professional Knife &amp; Tool Sharpening in Stevenson Ranch</h1>
    <p>Fast, precise sharpening for knives, scissors, and garden tools.</p>
    <span class="btn-call">Call Now (661-555-0173)</span>
  </div>
</header>

<section class="about">
  <div class="about-copy">
    <h2 class="section-title">Restoring the Edge to Your Daily Tools</h2>
    <div class="rule"></div>
    <p>At Bay Bolt, we understand that a dull blade is not just frustrating, but dangerous. We bring professional-grade sharpening techniques directly to your kitchen and workshop tools. Our meticulous process ensures that every edge we touch is restored to its original glory, providing you with precision and ease in every cut.</p>
    <p>Whether you are a professional chef requiring razor-sharp Japanese steel or a home gardener needing to revive old shears, we treat every tool with the utmost care. Experience the difference that a truly sharp edge can make in your daily tasks.</p>
  </div>
  <div class="about-frame"></div>
  <div class="about-photo" role="img" aria-label="Black and white photo of hands sharpening a chef's knife on a whetstone"></div>
</section>

<section class="services">
  <h2 class="section-title center-title">Services</h2>
  <div class="rule-center"></div>
  <div class="cards">
    <div class="card">
      <svg viewBox="0 0 46 46" fill="none" stroke="#c9a25a" stroke-width="2.5" stroke-linecap="round">
        <line x1="9" y1="4" x2="9" y2="42"/><line x1="23" y1="4" x2="23" y2="42"/><line x1="37" y1="4" x2="37" y2="42"/>
        <circle cx="9" cy="28" r="4" fill="#fff"/><circle cx="23" cy="14" r="4" fill="#fff"/><circle cx="37" cy="24" r="4" fill="#fff"/>
      </svg>
      <h3>Kitchen Knives</h3>
      <p>We sharpen all types of culinary blades, from standard chef's knives to serrated bread knives and high-end Japanese steel, restoring a factory-quality edge.</p>
    </div>
    <div class="card">
      <svg viewBox="0 0 46 46" fill="none" stroke="#c9a25a" stroke-width="2.5" stroke-linecap="round">
        <circle cx="10" cy="12" r="6"/><circle cx="10" cy="34" r="6"/>
        <line x1="15" y1="15" x2="43" y2="32"/><line x1="15" y1="31" x2="43" y2="8"/>
      </svg>
      <h3>Scissors &amp; Shears</h3>
      <p>From fabric shears to household scissors, we realign and sharpen blades to ensure smooth, clean cuts without folding or tearing materials.</p>
    </div>
    <div class="card">
      <svg viewBox="0 0 46 46" fill="none" stroke="#c9a25a" stroke-width="2.5" stroke-linecap="round">
        <circle cx="27" cy="12" r="8"/><path d="M22 18 L6 40"/><path d="M30 19 Q34 32 42 40"/><path d="M6 40 Q14 38 20 30"/>
      </svg>
      <h3>Garden Tools</h3>
      <p>Keep your garden thriving with sharp pruners, loppers, and hedge trimmers. Sharp tools make cleaner cuts that heal faster and require less effort.</p>
    </div>
  </div>
</section>

<section class="pricing">
  <h2 class="section-title center-title">Pricing</h2>
  <div class="rule-center"></div>
  <ul class="price-list">
    <li><span class="item">Standard Knife (up to 5")</span><span class="cost">$6.00</span></li>
    <li><span class="item">Standard Knife (up to 2")</span><span class="cost">$6.00</span></li>
    <li><span class="item">Standard Knife (Over 6")</span><span class="cost">$12.00</span></li>
    <li><span class="item">French Bags</span><span class="cost">$14.00</span></li>
    <li><span class="item">Garden Tools</span><span class="cost">$16.00</span></li>
  </ul>
  <p class="note">* Prices may vary based on condition and specific requirements.</p>
</section>

<section class="contact" role="img" aria-label="Blurred photo of a sharpening workshop interior">
  <div class="contact-panel">
    <div class="form">
      <h2 class="section-title">Get In Touch</h2>
      <span class="field-label">Your Name</span>
      <div class="input">John Doe</div>
      <span class="field-label">Phone Number</span>
      <div class="input">(555) 123-4567</div>
      <span class="field-label">How can we help?</span>
      <div class="input area">I have 3 kitchen knives that need sharpening...</div>
      <div class="send">SEND REQUEST</div>
    </div>
    <div class="visit">
      <h3 class="section-title">Visit Us</h3>
      <p class="biz">Bay Bolt Workshop</p>
      <address>18302 Pellman Way<br>Stevenson Ranch, CA 91381</address>
      <p class="phone">661-555-0173</p>
    </div>
    <div class="map" role="img" aria-label="Illustrated street map with a red location pin"></div>
  </div>
</section>

<footer class="site-footer">
  <div>
    <div class="footer-brand">Bay Bolt</div>
    <div class="footer-tag">Professional Sharpening Services</div>
  </div>
  <div class="footer-meta">© 2026 Bay Bolt. All rights reserved.<br>Stevenson Ranch, CA</div>
</footer>

</body>
</html>
```